Corporate Power Point Template

Tarrowmead Group, Inc. produces and sells ready-mixed concrete, aggregates, and concrete-related products and services for the construction industry in the United States.

We are looking for a simple and sleek design that will look great on a projector, as well as when printed on paper. We prefer a lighter background color that will not waste ink when printed. We would also like to stay away from wavy banners, or over-the-top graphics that take away from usable space in the deck. Please use a variation of the color scheme in the "Brand Standards" file attached.

```html
<!DOCTYPE html>
<html lang="en">
<head>
<meta charset="utf-8">
<title>Tarrowmead Group – Corporate Presentation Template</title>
<link href="https://fonts.googleapis.com/css2?family=Roboto:wght@300;400;500&display=swap" rel="stylesheet">
<style>
:root{
  --red:#c20e2f;
  --red-deep:#8c0a20;
  --ink:#1c1c1c;
  --charcoal:#3a3a3a;
  --steel:#7b7b7b;
  --ash:#9a9a9a;
  --mist:#d8d8d8;
  --haze:#ededed;
  --paper:#ffffff;
  --band:#8c8c8c;
  --band-dark:#6b6b6b;
}
html,body{margin:0;padding:0;background:var(--paper);overflow:hidden}
.board{position:relative;width:1200px;height:1141px;overflow:hidden;background:var(--paper);font-family:'Roboto',Arial,sans-serif}
.slide{position:absolute;width:398px;height:226px;background:var(--paper);overflow:hidden;box-shadow:0 1px 3px rgba(0,0,0,.35)}
.slide-art{position:absolute;left:0;top:0;width:398px;height:226px}
.slide-title{position:absolute;left:18px;top:10px;margin:0;font-weight:300;font-size:18px;line-height:20px;color:#222;letter-spacing:-.2px}
.title-rule{position:absolute;left:0;right:0;top:35px;height:1px;background:#e6e6e6}
.title-rule::before{content:"";position:absolute;left:18px;top:-1px;width:24px;height:2px;background:var(--red)}
.brand{position:absolute;right:12px;top:9px;display:flex;align-items:center;gap:3px;font-weight:500;font-size:8px;letter-spacing:.5px;color:#6e6e6e}
.brand-mark{width:6px;height:6px;background:var(--red)}
.footer{position:absolute;left:0;right:0;bottom:0;height:8px;background:var(--band)}
.footer-tab{position:absolute;left:0;bottom:0;width:17px;height:14px;background:var(--band-dark)}
.page-no{position:absolute;left:22px;bottom:2px;font-size:3.5px;color:#fff}
.copyright{position:absolute;right:8px;bottom:2px;font-size:3.5px;color:#f2f2f2}
svg text{font-family:'Roboto',Arial,sans-serif}
.lorem{font-size:3.4px;fill:#a9a9a9}
.lorem-light{font-size:3.2px;fill:#f4f4f4}
.lbl{font-size:6px;fill:#3a3a3a}
.lbl-red{font-size:6px;fill:var(--red)}
.tiny{font-size:3px;fill:#888}
.big-num{font-size:12px;font-weight:300;fill:#555}
</style>
</head>
<body>
<div class="board">

<!-- Customer testimonials -->
<section class="slide" style="left:0;top:0">
  <svg class="slide-art" viewBox="0 0 398 226">
    <defs>
      <radialGradient id="portraitTone" cx="50%" cy="40%" r="60%"><stop offset="0" stop-color="#c9b8a8"/><stop offset="1" stop-color="#5c5650"/></radialGradient>
    </defs>
    <g role="img" aria-label="Customer portrait photograph"><circle cx="112" cy="67" r="27" fill="url(#portraitTone)"/></g>
    <text class="lorem" x="172" y="60">adipiscing elit, sed diam nonummy nibh euismod tincidunt ut laoreet</text>
    <text class="lorem" x="172" y="66">dolore magna aliquam erat volutpat. Ut wisi enim <tspan fill="#555">Lorem</tspan></text>
    <text class="lorem" x="172" y="72"><tspan fill="#555">ipsum</tspan> dolor sit amet, consectetuer adipiscing elit, sed diam nonummy</text>
    <text class="lorem" x="172" y="78">nibh euismod tincidunt ut laoreet dolore magna.</text>
    <rect x="0" y="112" width="398" height="106" fill="var(--steel)"/>
    <polygon points="105,112 112,105 119,112" fill="var(--steel)"/>
    <g fill="none" stroke="#fff" stroke-width=".8">
      <circle cx="95" cy="148" r="14"/><circle cx="170" cy="148" r="14"/><circle cx="245" cy="148" r="14"/><circle cx="323" cy="148" r="14"/>
      <rect x="89" y="143" width="12" height="9"/><path d="M92 155h6"/>
      <rect x="164" y="142" width="12" height="11" rx="1.5"/><circle cx="170" cy="147.5" r="2.5"/>
      <rect x="239" y="142" width="12" height="12"/><path d="M240 153l10-10M240 149l6-6M244 153l6-6"/>
      <rect x="317" y="142" width="12" height="12"/><path d="M317 146h12M321 146v8M325 146v8"/>
    </g>
    <g text-anchor="middle">
      <text class="lorem-light" x="95" y="176">Why does getting a loan</text>
      <text class="lorem-light" x="95" y="180">have to be so much more</text>
      <text class="lorem-light" x="95" y="184">complicated than ordering</text>
      <text class="lorem-light" x="95" y="188">a fridge online?</text>
      <text class="lorem-light" x="170" y="176">Why do I have to go to</text>
      <text class="lorem-light" x="170" y="180">a branch, fill out forms</text>
      <text class="lorem-light" x="170" y="184">and wait for weeks to</text>
      <text class="lorem-light" x="170" y="188">get a response?</text>
      <text class="lorem-light" x="245" y="176">Why do banks refuse</text>
      <text class="lorem-light" x="245" y="180">to lend to me despite</text>
      <text class="lorem-light" x="245" y="184">the substantial fees I</text>
      <text class="lorem-light" x="245" y="188">receive each month?</text>
      <text class="lorem-light" x="323" y="176">Why is there no store</text>
      <text class="lorem-light" x="323" y="180">in lending that identifies</text>
      <text class="lorem-light" x="323" y="184">my needs and offers</text>
      <text class="lorem-light" x="323" y="188">convenience at fair prices?</text>
    </g>
  </svg>
  <h2 class="slide-title">CUSTOMER TESTIMONIALS</h2>
  <div class="title-rule"></div>
  <div class="brand"><span class="brand-mark"></span>TARROWMEAD</div>
  <div class="footer"><div class="footer-tab"></div><span class="page-no">46</span><span class="copyright">© 2017 TARROWMEAD GROUP  All rights reserved.</span></div>
</section>

<!-- Financial report -->
<section class="slide" style="left:401px;top:0">
  <svg class="slide-art" viewBox="0 0 398 226">
    <path d="M183 90A70 36 0 0 1 44.1 96.3L44.1 106.3A70 36 0 0 0 183 100Z" fill="var(--red-deep)"/>
    <path d="M113 90L125.2 54.5A70 36 0 1 1 44.1 96.3Z" fill="var(--red)"/>
    <g transform="translate(-8,3)">
      <path d="M44.1 96.3L44.1 106.3L113 100L113 90Z" fill="#4f4f4f"/>
      <path d="M113 90L44.1 96.3A70 36 0 0 1 55.7 69.3Z" fill="var(--steel)"/>
    </g>
    <path d="M113 90L55.7 69.3A70 36 0 0 1 125.2 54.5Z" fill="var(--ink)"/>
    <g class="tiny">
      <rect x="85" y="142.5" width="2.5" height="2.5" fill="var(--red)"/><text x="89" y="145">Sales A</text>
      <rect x="106" y="142.5" width="2.5" height="2.5" fill="var(--steel)"/><text x="110" y="145">Sales B</text>
      <rect x="127" y="142.5" width="2.5" height="2.5" fill="var(--ink)"/><text x="131" y="145">Sales C</text>
    </g>
    <polygon points="12,180 17.5,171 23,180" fill="var(--red)"/>
    <text x="25" y="181" font-size="16" font-weight="300" fill="#333">54%</text>
    <text x="77" y="168" font-size="5.5" fill="#444">Heading Goes Here</text>
    <text class="lorem" x="77" y="174">Lorem ipsum adipiscing elit, sed do eiusmod tempor</text>
    <text class="lorem" x="77" y="179">incididunt ut labore et dolore magna aliqua. Ut enim ad</text>
    <text class="lorem" x="77" y="184">minim veniam, quis nostrud exercitation ullamco laboris nisi</text>
    <text class="lorem" x="77" y="189">ut aliquip ex ea commodo consequat.</text>
    <circle cx="225" cy="51" r="6" fill="var(--red)"/>
    <circle cx="225" cy="84" r="6" fill="var(--ash)"/>
    <circle cx="225" cy="117" r="6" fill="var(--ink)"/>
    <circle cx="225" cy="150" r="6" fill="var(--charcoal)"/>
    <g fill="#fff"><circle cx="225" cy="51" r="2"/><circle cx="225" cy="84" r="2"/><circle cx="225" cy="117" r="2"/><circle cx="225" cy="150" r="2"/></g>
    <text class="lbl-red" x="236" y="50">Your Text Here</text>
    <text class="lorem" x="236" y="56">Lorem ipsum dolor sit amet.</text>
    <text class="lbl" x="236" y="83" fill="#777">Your Text Here</text>
    <text class="lorem" x="236" y="89">Lorem ipsum dolor sit amet.</text>
    <text class="lbl" x="236" y="116" fill="#777">Your Text Here</text>
    <text class="lorem" x="236" y="122">Lorem ipsum dolor sit amet.</text>
    <text class="lbl" x="236" y="149" fill="#777">Your Text Here</text>
    <text class="lorem" x="236" y="155">Lorem ipsum dolor sit amet.</text>
  </svg>
  <h2 class="slide-title">FINANCIAL REPORT</h2>
  <div class="title-rule"></div>
  <div class="brand"><span class="brand-mark"></span>TARROWMEAD</div>
  <div class="footer"><div class="footer-tab"></div><span class="page-no">47</span><span class="copyright">© 2017 TARROWMEAD GROUP  All rights reserved.</span></div>
</section>

<!-- Bullet & chart area (bars) -->
<section class="slide" style="left:802px;top:0">
  <svg class="slide-art" viewBox="0 0 398 226">
    <g class="tiny" text-anchor="end">
      <text x="57" y="72">Category 4</text><text x="57" y="101">Category 3</text><text x="57" y="130">Category 2</text><text x="57" y="159">Category 1</text>
    </g>
    <g>
      <rect x="61" y="62" width="105" height="4.5" fill="var(--ink)"/><rect x="61" y="67" width="60" height="4.5" fill="var(--steel)"/><rect x="61" y="72" width="95" height="4.5" fill="var(--red)"/>
      <rect x="61" y="91" width="65" height="4.5" fill="var(--ink)"/><rect x="61" y="96" width="38" height="4.5" fill="var(--steel)"/><rect x="61" y="101" width="75" height="4.5" fill="var(--red)"/>
      <rect x="61" y="120" width="52" height="4.5" fill="var(--ink)"/><rect x="61" y="125" width="93" height="4.5" fill="var(--steel)"/><rect x="61" y="130" width="52" height="4.5" fill="var(--red)"/>
      <rect x="61" y="149" width="63" height="4.5" fill="var(--ink)"/><rect x="61" y="154" width="47" height="4.5" fill="var(--steel)"/><rect x="61" y="159" width="92" height="4.5" fill="var(--red)"/>
    </g>
    <g class="tiny">
      <rect x="86" y="178" width="2.5" height="2.5" fill="var(--ink)"/><text x="90" y="180.5">Series 3</text>
      <rect x="104" y="178" width="2.5" height="2.5" fill="var(--steel)"/><text x="108" y="180.5">Series 2</text>
      <rect x="122" y="178" width="2.5" height="2.5" fill="var(--red)"/><text x="126" y="180.5">Series 1</text>
    </g>
    <circle cx="225" cy="67" r="7" fill="var(--red)"/>
    <circle cx="225" cy="100" r="7" fill="var(--ash)"/>
    <circle cx="225" cy="132" r="7" fill="var(--ink)"/>
    <circle cx="225" cy="164" r="7" fill="var(--charcoal)"/>
    <g fill="none" stroke="#fff" stroke-width=".9">
      <circle cx="224" cy="66" r="2"/><path d="M225.5 67.5l2 2"/>
      <path d="M222.5 102.5l5-5"/>
      <path d="M222.5 134.5l2-4 3-1-1 3-4 2z"/>
      <circle cx="225" cy="164" r="2.2"/>
    </g>
    <text class="lbl-red" x="237" y="66">Category One</text>
    <text class="lorem" x="237" y="71">Lorem ipsum dolor sit amet, consectetur</text><text class="lorem" x="237" y="75">adipiscing elit, sed do eiusmod.</text>
    <text class="lbl" x="237" y="99" fill="#666">Category Two</text>
    <text class="lorem" x="237" y="104">Lorem ipsum dolor sit amet, consectetur</text><text class="lorem" x="237" y="108">adipiscing elit, sed do eiusmod.</text>
    <text class="lbl" x="237" y="131" fill="#666">Category Three</text>
    <text class="lorem" x="237" y="136">Lorem ipsum dolor sit amet, consectetur</text><text class="lorem" x="237" y="140">adipiscing elit, sed do eiusmod.</text>
    <text class="lbl" x="237" y="163" fill="#666">Category Four</text>
    <text class="lorem" x="237" y="168">Lorem ipsum dolor sit amet, consectetur</text><text class="lorem" x="237" y="172">adipiscing elit, sed do eiusmod.</text>
  </svg>
  <h2 class="slide-title">BULLET &amp; CHART AREA</h2>
  <div class="title-rule"></div>
  <div class="brand"><span class="brand-mark"></span>TARROWMEAD</div>
  <div class="footer"><div class="footer-tab"></div><span class="page-no">48</span><span class="copyright">© 2017 TARROWMEAD GROUP  All rights reserved.</span></div>
</section>

<!-- Triangle infographic -->
<section class="slide" style="left:0;top:229px">
  <svg class="slide-art" viewBox="0 0 398 226">
    <ellipse cx="118" cy="176" rx="70" ry="7" fill="#000" opacity=".12"/>
    <polygon points="118,46 136.8,82 99.2,82" fill="var(--charcoal)"/>
    <polygon points="99.2,82 136.8,82 150.5,108 85.5,108" fill="var(--ash)"/>
    <polygon points="85.5,108 150.5,108 162,130 74,130" fill="var(--ink)"/>
    <polygon points="74,130 162,130 172.4,150 63.6,150" fill="var(--ash)"/>
    <polygon points="63.6,150 172.4,150 185,174 51,174" fill="var(--red)"/>
    <polygon points="118,46 185,174 130,174" fill="#000" opacity=".16"/>
    <circle cx="151" cy="66" r="8" fill="var(--charcoal)"/>
    <circle cx="164" cy="96" r="8" fill="var(--ink)"/>
    <circle cx="182" cy="126" r="8" fill="#fff" stroke="var(--mist)"/>
    <circle cx="199" cy="158" r="8" fill="var(--red)"/>
    <g fill="none" stroke="#fff" stroke-width=".8">
      <rect x="147.5" y="63" width="7" height="5"/><path d="M149 70h4"/>
      <path d="M161.5 98.5l5-5"/>
      <path d="M195.5 159.5l3.5-3 3.5 3v3h-7z"/>
    </g>
    <path d="M178.5 124h7l-1 4h-5z" fill="none" stroke="var(--ash)" stroke-width=".7"/>
    <text x="163" y="64" font-size="7" fill="#444">Content Title</text>
    <text class="lorem" x="163" y="70">Lorem ipsum dolor sit amet, consectetur adipiscing elit. Nunc</text><text class="lorem" x="163" y="75">bibendum eleifend tortor.</text>
    <text x="176" y="94" font-size="7" fill="#444">Content Title</text>
    <text class="lorem" x="176" y="100">Lorem ipsum dolor sit amet, consectetur adipiscing elit. Nunc</text><text class="lorem" x="176" y="105">bibendum eleifend tortor.</text>
    <text x="194" y="124" font-size="7" fill="#888">Content Title</text>
    <text class="lorem" x="194" y="130">Lorem ipsum dolor sit amet, consectetur adipiscing elit. Nunc</text><text class="lorem" x="194" y="135">bibendum eleifend tortor.</text>
    <text x="211" y="156" font-size="7" fill="var(--red)">Content Title</text>
    <text class="lorem" x="211" y="162">Lorem ipsum dolor sit amet, consectetur adipiscing elit. Nunc</text><text class="lorem" x="211" y="167">bibendum eleifend tortor.</text>
  </svg>
  <h2 class="slide-title">TRIANGLE INFOGRAPHIC</h2>
  <div class="title-rule"></div>
  <div class="brand"><span class="brand-mark"></span>TARROWMEAD</div>
  <div class="footer"><div class="footer-tab"></div><span class="page-no">49</span><span class="copyright">© 2017 TARROWMEAD GROUP  All rights reserved.</span></div>
</section>

<!-- Digital system -->
<section class="slide" style="left:401px;top:229px">
  <svg class="slide-art" viewBox="0 0 398 226">
    <g fill="none" stroke-width="28">
      <circle cx="199" cy="116" r="56" pathLength="100" stroke="var(--steel)" stroke-dasharray="15.8 84.2" transform="rotate(-89 199 116)"/>
      <circle cx="199" cy="116" r="56" pathLength="100" stroke="var(--ink)" stroke-dasharray="15.8 84.2" transform="rotate(-29 199 116)"/>
      <circle cx="199" cy="116" r="56" pathLength="100" stroke="var(--red)" stroke-dasharray="15.8 84.2" transform="rotate(31 199 116)"/>
      <circle cx="199" cy="116" r="56" pathLength="100" stroke="var(--steel)" stroke-dasharray="15.8 84.2" transform="rotate(91 199 116)"/>
      <circle cx="199" cy="116" r="56" pathLength="100" stroke="var(--ink)" stroke-dasharray="15.8 84.2" transform="rotate(151 199 116)"/>
      <circle cx="199" cy="116" r="56" pathLength="100" stroke="var(--red)" stroke-dasharray="15.8 84.2" transform="rotate(211 199 116)"/>
    </g>
    <text x="199" y="118" text-anchor="middle" font-size="5.5" font-weight="500" fill="var(--red)">TARROWMEAD</text>
    <g text-anchor="end">
      <text class="lbl-red" font-size="5" x="120" y="51">Layer</text>
      <text class="lorem" x="120" y="57">Vestibulum neque elit. Class aptent</text><text class="lorem" x="120" y="61">taciti sociosqu ad litora torquent per</text><text class="lorem" x="120" y="65">conubia nostra, per inceptos.</text>
      <text class="lbl" font-size="5" x="120" y="107">Building</text>
      <text class="lorem" x="120" y="113">Vestibulum neque elit. Class aptent</text><text class="lorem" x="120" y="117">taciti sociosqu ad litora torquent per</text><text class="lorem" x="120" y="121">conubia nostra, per inceptos.</text>
      <text class="lbl" font-size="5" x="120" y="163">Umbrella</text>
      <text class="lorem" x="120" y="169">Vestibulum neque elit. Class aptent</text><text class="lorem" x="120" y="173">taciti sociosqu ad litora torquent per</text><text class="lorem" x="120" y="177">conubia nostra, per inceptos.</text>
    </g>
    <text class="lbl" font-size="5" x="284" y="51">Battery</text>
    <text class="lorem" x="284" y="57">Vestibulum neque elit. Class aptent</text><text class="lorem" x="284" y="61">taciti sociosqu ad litora torquent per</text><text class="lorem" x="284" y="65">conubia nostra, per inceptos.</text>
    <text class="lbl" font-size="5" x="284" y="107">Calendar</text>
    <text class="lorem" x="284" y="113">Vestibulum neque elit. Class aptent</text><text class="lorem" x="284" y="117">taciti sociosqu ad litora torquent per</text><text class="lorem" x="284" y="121">conubia nostra, per inceptos.</text>
    <text class="lbl-red" font-size="5" x="284" y="163">Chart</text>
    <text class="lorem" x="284" y="169">Vestibulum neque elit. Class aptent</text><text class="lorem" x="284" y="173">taciti sociosqu ad litora torquent per</text><text class="lorem" x="284" y="177">conubia nostra, per inceptos.</text>
    <g fill="var(--red)"><rect x="125" y="50" width="12" height="2"/><rect x="125" y="54" width="12" height="2"/><rect x="125" y="58" width="12" height="2"/></g>
    <rect x="129" y="105" width="6" height="11" fill="var(--ink)"/>
    <path d="M126 170a7 6 0 0 1 14 0zM133 170v7" fill="none" stroke="var(--charcoal)" stroke-width="1"/>
    <rect x="263" y="50" width="12" height="7" fill="none" stroke="var(--ink)" stroke-width="1"/>
    <rect x="263" y="104" width="12" height="10" fill="none" stroke="var(--ink)" stroke-width="1"/>
    <path d="M263 107h12M266 104v10M269 104v10M272 104v10" stroke="var(--ink)" stroke-width=".6"/>
    <rect x="263" y="160" width="11" height="8" fill="var(--red)"/><path d="M268.5 168v4" stroke="var(--red)"/>
  </svg>
  <h2 class="slide-title">DIGITAL SYSTEM</h2>
  <div class="title-rule"></div>
  <div class="brand"><span class="brand-mark"></span>TARROWMEAD</div>
  <div class="footer"><div class="footer-tab"></div><span class="page-no">50</span><span class="copyright">© 2017 TARROWMEAD GROUP  All rights reserved.</span></div>
</section>

<!-- Advanced -->
<section class="slide" style="left:802px;top:229px">
  <svg class="slide-art" viewBox="0 0 398 226">
    <path d="M139 103V80Q139 48 171 48H194V103Z" fill="var(--charcoal)"/>
    <path d="M198 48H221Q253 48 253 80V103H198Z" fill="var(--red)"/>
    <path d="M253 107V130Q253 162 221 162H198V107Z" fill="var(--ash)"/>
    <path d="M194 162H171Q139 162 139 130V107H194Z" fill="var(--ink)"/>
    <circle cx="196" cy="105" r="21" fill="#fff"/>
    <text x="196" y="107" text-anchor="middle" font-size="4.6" font-weight="500" fill="var(--red)">TARROWMEAD</text>
    <g text-anchor="end">
      <text class="lbl" font-size="5" x="100" y="69">Warning</text>
      <text class="lorem" x="100" y="75">Nullam eu tempor purus. Nunc a</text><text class="lorem" x="100" y="79">leo magna, sit amet consequat</text><text class="lorem" x="100" y="83">risus. Etiam faucibus tortor.</text>
      <text class="lbl" font-size="5" x="100" y="123">Digital</text>
      <text class="lorem" x="100" y="129">Nullam eu tempor purus. Nunc a</text><text class="lorem" x="100" y="133">leo magna, sit amet consequat</text><text class="lorem" x="100" y="137">risus. Etiam faucibus tortor.</text>
    </g>
    <text class="lbl-red" font-size="5" x="294" y="69">Mobile</text>
    <text class="lorem" x="294" y="75">Nullam eu tempor purus. Nunc a</text><text class="lorem" x="294" y="79">leo magna, sit amet consequat</text><text class="lorem" x="294" y="83">risus. Etiam faucibus tortor.</text>
    <text class="lbl" font-size="5" x="294" y="123">Security</text>
    <text class="lorem" x="294" y="129">Nullam eu tempor purus. Nunc a</text><text class="lorem" x="294" y="133">leo magna, sit amet consequat</text><text class="lorem" x="294" y="137">risus. Etiam faucibus tortor.</text>
    <path d="M109 72a8 6 0 0 1 16 0zM117 72v9" fill="none" stroke="var(--charcoal)" stroke-width="1.2"/>
    <path d="M109 124l8-7 8 7h-2v7h-12v-7z" fill="var(--ink)"/>
    <circle cx="275" cy="70" r="5" fill="none" stroke="var(--red)" stroke-width="1.4"/><path d="M273 76h4v3h-4z" fill="var(--red)"/>
    <rect x="269" y="121" width="13" height="9" rx="1" fill="#555"/><rect x="273" y="118.5" width="5" height="3" fill="none" stroke="#555"/>
  </svg>
  <h2 class="slide-title">ADVANCED</h2>
  <div class="title-rule"></div>
  <div class="brand"><span class="brand-mark"></span>TARROWMEAD</div>
  <div class="footer"><div class="footer-tab"></div><span class="page-no">51</span><span class="copyright">© 2017 TARROWMEAD GROUP  All rights reserved.</span></div>
</section>

<!-- Table -->
<section class="slide" style="left:0;top:458px">
  <svg class="slide-art" viewBox="0 0 398 226">
    <text x="31" y="50" font-size="3" fill="#333"><tspan font-weight="500">Description :</tspan><tspan fill="#999"> There are many variations of passages of lorem ipsum available, but the majority have suffered alteration</tspan></text>
    <text x="31" y="54" font-size="3" fill="#999">in some form, by injected humour, or randomised words which don't look even slightly believable.</text>
    <rect x="27" y="61" width="342" height="11" fill="var(--steel)"/>
    <g font-size="3.6" fill="#fff" text-anchor="middle">
      <text x="60" y="68">Lorem ipsum</text><text x="130" y="68">Value</text><text x="198" y="68">Value</text><text x="267" y="68">Value</text><text x="336" y="68">Value</text>
    </g>
    <g>
      <rect x="27" y="72" width="342" height="12.6" fill="#f1f1f1"/><rect x="27" y="84.6" width="342" height="12.6" fill="#e6e6e6"/>
      <rect x="27" y="97.2" width="342" height="12.6" fill="#f1f1f1"/><rect x="27" y="109.8" width="342" height="12.6" fill="#e6e6e6"/>
      <rect x="27" y="122.4" width="342" height="12.6" fill="#f1f1f1"/><rect x="27" y="135" width="342" height="12.6" fill="#e6e6e6"/>
      <rect x="27" y="147.6" width="342" height="12.6" fill="#f1f1f1"/><rect x="27" y="160.2" width="342" height="12.6" fill="#e6e6e6"/>
      <rect x="27" y="172.8" width="342" height="12.6" fill="#f1f1f1"/>
    </g>
    <g stroke="#fff" stroke-width=".6"><path d="M110 61V185.4M175 61V185.4M240 61V185.4M305 61V185.4"/></g>
    <g font-size="3.2" fill="#888">
      <text x="48" y="80">Lorem ipsum</text><text x="48" y="92.6">Lorem ipsum</text><text x="48" y="105.2">Lorem ipsum</text><text x="48" y="117.8">Lorem ipsum</text><text x="48" y="130.4">Lorem ipsum</text><text x="48" y="143">Lorem ipsum</text><text x="48" y="155.6">Lorem ipsum</text><text x="48" y="168.2">Lorem ipsum</text><text x="48" y="180.8">Lorem ipsum</text>
    </g>
    <g font-size="4" fill="#888" text-anchor="middle">
      <text x="130" y="80">10</text><text x="198" y="80">15</text><text x="267" y="80">16</text><text x="336" y="80">18</text>
      <text x="130" y="92.6">12</text><text x="198" y="92.6">13</text><text x="267" y="92.6">15</text><text x="336" y="92.6">16</text>
      <text x="130" y="105.2">20</text><text x="198" y="105.2">22</text><text x="267" y="105.2">21</text><text x="336" y="105.2">21</text>
      <text x="130" y="117.8">10</text><text x="198" y="117.8">21</text><text x="267" y="117.8">12</text><text x="336" y="117.8">11</text>
      <text x="130" y="130.4">25</text><text x="198" y="130.4">25</text><text x="267" y="130.4">25</text><text x="336" y="130.4">25</text>
      <text x="130" y="143">10</text><text x="198" y="143">02</text><text x="267" y="143">51</text><text x="336" y="143">21</text>
      <text x="130" y="155.6">35</text><text x="198" y="155.6">35</text><text x="267" y="155.6">65</text><text x="336" y="155.6">32</text>
      <text x="130" y="168.2">26</text><text x="198" y="168.2">33</text><text x="267" y="168.2">35</text><text x="336" y="168.2">32</text>
      <text x="130" y="180.8">32</text><text x="198" y="180.8">10</text><text x="267" y="180.8">32</text><text x="336" y="180.8">32</text>
    </g>
  </svg>
  <h2 class="slide-title">YOUR TABLE HERE</h2>
  <div class="title-rule"></div>
  <div class="brand"><span class="brand-mark"></span>TARROWMEAD</div>
  <div class="footer"><div class="footer-tab"></div><span class="page-no">52</span><span class="copyright">© 2017 TARROWMEAD GROUP  All rights reserved.</span></div>
</section>

<!-- Our team -->
<section class="slide" style="left:401px;top:458px">
  <svg class="slide-art" viewBox="0 0 398 226">
    <defs>
      <radialGradient id="teamTone" cx="50%" cy="40%" r="60%"><stop offset="0" stop-color="#d9a88c"/><stop offset=".7" stop-color="#6b5648"/><stop offset="1" stop-color="#2a2a2a"/></radialGradient>
    </defs>
    <g role="img" aria-label="Portrait photograph of the chief executive"><circle cx="199" cy="89" r="47" fill="url(#teamTone)"/></g>
    <g text-anchor="middle">
      <text x="199" y="150" font-size="4.5" fill="#777">Mr. Dale Whitcombe</text>
      <text x="199" y="156" font-size="4.5" fill="var(--red)">CEO</text>
      <text class="lorem" x="199" y="162">Lorem ipsum dolor sit amet, consectetur adipiscing elit,</text>
      <text class="lorem" x="199" y="166">sed do eiusmod tempor incididunt ut labore et dolore</text>
      <text class="lorem" x="199" y="170">magna aliqua. Ut enim ad minim veniam, quis nostrud.</text>
      <text class="lorem" x="199" y="174">Duis aute irure dolor in reprehenderit in voluptate velit</text>
      <text class="lorem" x="199" y="178">esse cillum dolore eu fugiat nulla pariatur.</text>
    </g>
    <g fill="var(--red)"><circle cx="184" cy="194" r="3.2"/><circle cx="194" cy="194" r="3.2"/><circle cx="204" cy="194" r="3.2"/><circle cx="214" cy="194" r="3.2"/></g>
  </svg>
  <h2 class="slide-title">OUR TEAM</h2>
  <div class="title-rule"></div>
  <div class="brand"><span class="brand-mark"></span>TARROWMEAD</div>
  <div class="footer"><div class="footer-tab"></div><span class="page-no">53</span><span class="copyright">© 2017 TARROWMEAD GROUP  All rights reserved.</span></div>
</section>

<!-- USA map -->
<section class="slide" style="left:802px;top:458px">
  <svg class="slide-art" viewBox="0 0 398 226">
    <defs>
      <linearGradient id="usMapTone" x1="0" y1="0" x2="1" y2="1"><stop offset="0" stop-color="#dcdcdc"/><stop offset="1" stop-color="#c4c4c4"/></linearGradient>
    </defs>
    <g role="img" aria-label="Map of the United States with highlighted states"><rect x="35" y="44" width="200" height="136" rx="6" fill="url(#usMapTone)"/></g>
    <rect x="261" y="55" width="78" height="22" fill="var(--red)"/>
    <rect x="261" y="83" width="78" height="22" fill="var(--steel)"/>
    <rect x="261" y="111" width="78" height="22" fill="var(--ink)"/>
    <rect x="261" y="139" width="78" height="22" fill="#4a4a4a"/>
    <g fill="none" stroke="#fff" stroke-width=".8">
      <circle cx="270" cy="66" r="4"/><circle cx="270" cy="94" r="4"/><circle cx="270" cy="122" r="4"/><circle cx="270" cy="150" r="4"/>
    </g>
    <g fill="#fff">
      <text x="280" y="64" font-size="5.5">80%</text><text x="280" y="70" font-size="3.2">All about sample will go here</text>
      <text x="280" y="92" font-size="5.5">60%</text><text x="280" y="98" font-size="3.2">All about sample will go here</text>
      <text x="280" y="120" font-size="5.5">30%</text><text x="280" y="126" font-size="3.2">All about sample will go here</text>
      <text x="280" y="148" font-size="5.5">20%</text><text x="280" y="154" font-size="3.2">All about sample will go here</text>
    </g>
  </svg>
  <h2 class="slide-title">USA MAP</h2>
  <div class="title-rule"></div>
  <div class="brand"><span class="brand-mark"></span>TARROWMEAD</div>
  <div class="footer"><div class="footer-tab"></div><span class="page-no">54</span><span class="copyright">© 2017 TARROWMEAD GROUP  All rights reserved.</span></div>
</section>

<!-- Global experience -->
<section class="slide" style="left:0;top:687px">
  <svg class="slide-art" viewBox="0 0 398 226">
    <g role="img" aria-label="World map"><rect x="24" y="105" width="353" height="52" rx="8" fill="#dcdcdc"/></g>
    <text x="49" y="70" font-size="9" fill="var(--red)">North America</text>
    <text x="92" y="89" font-size="9" fill="#666">South America</text>
    <text x="190" y="80" font-size="9" fill="#444">Europe</text>
    <text x="277" y="89" font-size="9" fill="#444">Asia</text>
    <g stroke-width=".6">
      <path d="M80 73V114" stroke="var(--red)"/>
      <path d="M122 92V136" stroke="#888"/>
      <path d="M206 83V112" stroke="#888"/>
      <path d="M287 92V115" stroke="#888"/>
    </g>
    <g fill="var(--red)"><circle cx="77" cy="117" r="2.2"/><circle cx="83" cy="117" r="2.2"/></g>
    <g fill="var(--charcoal)">
      <circle cx="119" cy="139" r="2.2"/><circle cx="125" cy="139" r="2.2"/>
      <circle cx="203" cy="115" r="2.2"/><circle cx="209" cy="115" r="2.2"/>
      <circle cx="281" cy="118" r="2.2"/><circle cx="287" cy="118" r="2.2"/><circle cx="293" cy="118" r="2.2"/>
    </g>
  </svg>
  <h2 class="slide-title">GLOBAL EXPERIENCE</h2>
  <div class="title-rule"></div>
  <div class="brand"><span class="brand-mark"></span>TARROWMEAD</div>
  <div class="footer"><div class="footer-tab"></div><span class="page-no">55</span><span class="copyright">© 2017 TARROWMEAD GROUP  All rights reserved.</span></div>
</section>

<!-- Table area -->
<section class="slide" style="left:401px;top:687px">
  <svg class="slide-art" viewBox="0 0 398 226">
    <rect x="61" y="50" width="276" height="139" fill="#000" opacity=".08"/>
    <rect x="60" y="48" width="276" height="139" fill="#fff"/>
    <rect x="60" y="48" width="109" height="36" fill="var(--red)"/>
    <rect x="169" y="48" width="84" height="36" fill="var(--steel)"/>
    <rect x="253" y="48" width="83" height="36" fill="var(--ink)"/>
    <text x="67" y="71" font-size="6.5" fill="#fff">Description</text>
    <text x="211" y="62" font-size="6.5" fill="#fff" text-anchor="middle">Column 1</text>
    <text x="294" y="62" font-size="6.5" fill="#fff" text-anchor="middle">Column 2</text>
    <circle cx="211" cy="77" r="5" fill="#fff"/><circle cx="294" cy="77" r="5" fill="#fff"/>
    <path d="M209 79l4-4" stroke="var(--steel)" stroke-width=".8"/>
    <path d="M291.5 78.5h5l.5-3-1.5 1-1.5-2-1.5 2-1.5-1z" fill="var(--ink)"/>
    <g stroke="#e4e4e4" stroke-width=".5"><path d="M169 84V187M253 84V187"/></g>
    <g stroke="#cfcfcf" stroke-width=".4">
      <path d="M67 108H163M67 117.5H163M67 127H163M67 136.5H163M67 146H163M67 155.5H163M67 165H163M67 174.5H163"/>
      <path d="M176 108H246M176 117.5H246M176 127H246M176 136.5H246M176 146H246M176 155.5H246M176 165H246M176 174.5H246"/>
      <path d="M260 108H330M260 117.5H330M260 127H330M260 136.5H330M260 146H330M260 155.5H330M260 165H330M260 174.5H330"/>
    </g>
    <g font-size="3.6" fill="#888">
      <text x="67" y="106">Description 1</text><text x="67" y="115.5">Description 2</text><text x="67" y="125">Description 3</text><text x="67" y="134.5">Description 4</text>
      <text x="67" y="144">Description 5</text><text x="67" y="153.5">Description 6</text><text x="67" y="163">Description 7</text><text x="67" y="172.5">Description 8</text>
    </g>
    <g fill="var(--ink)">
      <circle cx="211" cy="104.5" r="1.3"/><circle cx="211" cy="114" r="1.3"/><circle cx="211" cy="133" r="1.3"/><circle cx="211" cy="171" r="1.3"/>
      <circle cx="294" cy="104.5" r="1.3"/><circle cx="294" cy="114" r="1.3"/><circle cx="294" cy="123.5" r="1.3"/><circle cx="294" cy="133" r="1.3"/><circle cx="294" cy="171" r="1.3"/>
    </g>
    <path d="M210 123.5h2" stroke="#999" stroke-width=".6"/>
    <g font-size="3.6" fill="#666" text-anchor="middle">
      <text x="211" y="144">Text Column 1</text><text x="211" y="163">Text Column 1</text>
      <text x="294" y="144">Text Column 2</text><text x="294" y="163">Text Column 2</text>
    </g>
  </svg>
  <h2 class="slide-title">TABLE AREA</h2>
  <div class="title-rule"></div>
  <div class="brand"><span class="brand-mark"></span>TARROWMEAD</div>
  <div class="footer"><div class="footer-tab"></div><span class="page-no">56</span><span class="copyright">© 2017 TARROWMEAD GROUP  All rights reserved.</span></div>
</section>

<!-- Bullet & chart area (donut) -->
<section class="slide" style="left:802px;top:687px">
  <svg class="slide-art" viewBox="0 0 398 226">
    <circle cx="47" cy="66" r="7.5" fill="var(--red)"/>
    <circle cx="47" cy="98" r="7.5" fill="var(--ash)"/>
    <circle cx="47" cy="130" r="7.5" fill="var(--ink)"/>
    <circle cx="47" cy="162" r="7.5" fill="var(--charcoal)"/>
    <g fill="none" stroke="#fff" stroke-width=".9">
      <circle cx="46" cy="65" r="2"/><path d="M47.5 66.5l2 2"/>
      <path d="M44.5 100.5l5-5"/>
      <path d="M44.5 132.5l2-4 3-1-1 3-4 2z"/>
      <circle cx="47" cy="162" r="2.3"/>
    </g>
    <text class="lbl-red" font-size="6.5" x="60" y="64">Your Text Here</text>
    <text class="lorem" x="60" y="70">Lorem ipsum dolor sit amet, consectetur</text><text class="lorem" x="60" y="74.5">adipiscing elit, sed do eiusmod.</text>
    <text class="lbl" font-size="6.5" x="60" y="96" fill="#777">Your Text Here</text>
    <text class="lorem" x="60" y="102">Lorem ipsum dolor sit amet, consectetur</text><text class="lorem" x="60" y="106.5">adipiscing elit, sed do eiusmod.</text>
    <text class="lbl" font-size="6.5" x="60" y="128" fill="#444">Your Text Here</text>
    <text class="lorem" x="60" y="134">Lorem ipsum dolor sit amet, consectetur</text><text class="lorem" x="60" y="138.5">adipiscing elit, sed do eiusmod.</text>
    <text class="lbl" font-size="6.5" x="60" y="160" fill="#777">Your Text Here</text>
    <text class="lorem" x="60" y="166">Lorem ipsum dolor sit amet, consectetur</text><text class="lorem" x="60" y="170.5">adipiscing elit, sed do eiusmod.</text>
    <g fill="none" stroke-width="10" transform="rotate(-90 286 124)">
      <circle cx="286" cy="124" r="42" pathLength="100" stroke="var(--red)" stroke-dasharray="55 45"/>
      <circle cx="286" cy="124" r="42" pathLength="100" stroke="var(--steel)" stroke-dasharray="22 78" stroke-dashoffset="-55"/>
      <circle cx="286" cy="124" r="42" pathLength="100" stroke="var(--ink)" stroke-dasharray="14 86" stroke-dashoffset="-77"/>
      <circle cx="286" cy="124" r="42" pathLength="100" stroke="var(--charcoal)" stroke-dasharray="9 91" stroke-dashoffset="-91"/>
    </g>
    <g fill="var(--ash)">
      <rect x="277" y="126" width="4" height="5"/><rect x="282" y="121" width="4" height="10"/><rect x="287" y="116" width="4" height="15"/><rect x="292" y="110" width="4" height="21"/>
      <rect x="275" y="132" width="23" height="1.2"/>
    </g>
    <text class="big-num" x="259" y="62">10%</text>
    <text class="big-num" x="220" y="94">15%</text>
    <text class="big-num" x="220" y="150">25%</text>
    <text class="big-num" x="338" y="122" fill="var(--red)">60%</text>
    <g class="tiny">
      <rect x="244" y="172.5" width="2" height="2" fill="var(--red)"/><text x="247.5" y="174.5">1st Qtr</text>
      <rect x="262" y="172.5" width="2" height="2" fill="var(--steel)"/><text x="265.5" y="174.5">2nd Qtr</text>
      <rect x="281" y="172.5" width="2" height="2" fill="var(--ink)"/><text x="284.5" y="174.5">3rd Qtr</text>
      <rect x="299" y="172.5" width="2" height="2" fill="var(--charcoal)"/><text x="302.5" y="174.5">4th Qtr</text>
    </g>
  </svg>
  <h2 class="slide-title">BULLET &amp; CHART AREA</h2>
  <div class="title-rule"></div>
  <div class="brand"><span class="brand-mark"></span>TARROWMEAD</div>
  <div class="footer"><div class="footer-tab"></div><span class="page-no">57</span><span class="copyright">© 2017 TARROWMEAD GROUP  All rights reserved.</span></div>
</section>

<!-- Thank you / contact -->
<section class="slide" style="left:401px;top:910px;height:228px">
  <svg class="slide-art" viewBox="0 0 398 228" style="height:228px">
    <defs>
      <linearGradient id="siteTone" x1="0" y1="0" x2="0" y2="1"><stop offset="0" stop-color="#6a6a6a"/><stop offset=".6" stop-color="#4e4e4e"/><stop offset="1" stop-color="#3a3a3a"/></linearGradient>
    </defs>
    <g role="img" aria-label="Photograph of a concrete mixer truck at a batching plant"><rect x="0" y="0" width="398" height="228" fill="url(#siteTone)"/></g>
    <rect x="235" y="0" width="140" height="228" fill="#262626"/>
    <text x="25" y="77" font-size="22" font-weight="300" fill="#fff">THANK YOU</text>
    <text x="42" y="93" font-size="6" fill="var(--red)">For Your Precious Time</text>
    <text x="29" y="104" font-size="6" fill="#f2f2f2">Stop by our office or give us a call</text>
    <text x="32" y="112" font-size="6" fill="#f2f2f2">We would love to hear from you.</text>
    <rect x="257" y="36" width="8" height="8" fill="var(--red)"/>
    <text x="268" y="44" font-size="12" font-weight="500" fill="#fff">TARROWMEAD</text>
    <text x="250" y="88" font-size="12" font-weight="300" fill="#fff">OUR CONTACT</text>
    <g fill="#fff">
      <path d="M249 116l3.5-3 3.5 3v3.5h-7z"/>
      <path d="M250 139.5a1 1 0 0 1 1.5-1l1 1.5-.7.8q.8 1.6 2.4 2.4l.8-.7 1.5 1a1 1 0 0 1-1 1.5q-4.5-.5-5.5-5.5z"/>
      <rect x="249" y="157" width="7" height="5"/>
      <circle cx="252.5" cy="177" r="3.2"/>
    </g>
    <path d="M249 157l3.5 3 3.5-3" stroke="#262626" stroke-width=".7" fill="none"/>
    <g font-size="6.2" fill="#fff">
      <text x="263" y="118">123 Street Road</text><text x="263" y="126">City  12345</text>
      <text x="263" y="144">(123) 456-7890</text>
      <text x="263" y="162">hello@tarrowmead.com</text>
      <text x="263" y="180">www.tarrowmead.com</text>
    </g>
    <rect x="235" y="203" width="140" height="20" fill="var(--red)"/>
    <g fill="#fff"><circle cx="291" cy="213" r="4.5"/><circle cx="305" cy="213" r="4.5"/><circle cx="319" cy="213" r="4.5"/></g>
  </svg>
</section>

</div>
</body>
</html>
```